Payday Lending App Interface Design

Hello, we are building a payday lending application, Lendora, that lend people money. I have drafted some of the screens that show the functionalities we have at the moment, please find the screens in attachments.
The elements in the screens are placed just to show what should be included in those screens, it's not necessary to follow the same layout. If you have better design ideas, you are very welcomed to show off your talent.
I think what we want is a style guide so that we can apply the same style to any screens that are similar to the ones I attached. We really like
the style as in the attached image called Style.png. We might want something similar - a simple, clean design yet fun and engaging. Customised graphical elements such as icons, illustrations are preferable.
Apart from the attached screens, we might also need a design for the On Board screen and the Login/Sign Up screen too.
Our logo colour is in yellow and black. Perhaps we will have a similar colour theme. I also attached the logo file, icon-Lendora.png, if you would like to put it in your design.
Please message me if you need further information.
Regards
Target Market(s)
Young people that doesn't have strong income
Look and feel

```html
<!DOCTYPE html>
<html lang="en">
<head>
<meta charset="utf-8">
<title>Lendora – App Screens</title>
<link href="https://fonts.googleapis.com/css2?family=Source+Sans+3:wght@400;600;700&display=swap" rel="stylesheet">
<style>
  :root {
    --board: #e4e3e1;
    --yellow: #fbd40b;
    --ink: #161616;
    --text: #2b2b2b;
    --muted: #444;
    --screen: #ffffff;
    --surface: #f4f3f4;
    --line: #cfcfcf;
    --dots: #e2e2e2;
  }
  * { box-sizing: border-box; margin: 0; padding: 0; }
  html, body { width: 770px; height: 1200px; overflow: hidden; }
  body {
    background: var(--board);
    font-family: "Source Sans 3", "Source Sans Pro", sans-serif;
    color: var(--text);
    position: relative;
  }
  .screen {
    position: absolute;
    width: 286px;
    background: var(--screen);
    overflow: hidden;
  }

  /* Loading screens */
  .loading { top: 57px; height: 508px; }
  .loading--left { left: 73px; }
  .loading--right { left: 404px; }
  .band {
    position: absolute; left: 0; right: 0; height: 11px; background: var(--yellow);
  }
  .band--top { top: 0; border-radius: 0 0 8px 8px; }
  .band--bottom { bottom: 0; border-radius: 8px 8px 0 0; }
  .brand {
    position: absolute; top: 148px; left: 0; right: 0;
    display: flex; align-items: center; justify-content: center; gap: 12px;
  }
  .brand__square { width: 60px; height: 60px; border-radius: 16px; background: var(--yellow); }
  .brand__name { font-size: 26px; font-weight: 700; color: var(--ink); }
  .loading__title {
    position: absolute; top: 262px; left: 0; right: 0; text-align: center;
    font-size: 19px; font-weight: 600; color: var(--ink);
  }
  .loading__body {
    position: absolute; top: 304px; left: 30px; right: 30px; text-align: center;
    font-size: 14px; line-height: 21px; color: var(--muted);
  }

  /* App screens with header */
  .app { top: 629px; height: 508px; background: var(--surface); }
  .app--left { left: 73px; }
  .app--right { left: 404px; }
  .header {
    height: 63px; background: var(--screen);
    display: flex; align-items: center; padding-left: 16px;
    box-shadow: 0 1px 3px rgba(0,0,0,.05);
  }
  .header__back { width: 14px; height: 14px; margin-right: 12px; }
  .header__brand { font-size: 13px; font-weight: 700; color: var(--ink); margin-right: 12px; }
  .header__title { font-size: 14.5px; font-weight: 600; color: var(--ink); line-height: 1.15; }
  .header__sub { font-size: 10.5px; color: var(--text); }

  .form { position: absolute; top: 0; left: 20px; right: 17px; }
  .field__label { position: absolute; left: 0; font-size: 11px; color: var(--text); }
  .field__input {
    position: absolute; left: 0; right: 0; height: 36px;
    background: #fff; border: 1px solid var(--line); border-radius: 8px;
  }
  .select {
    position: absolute; top: 358px; width: 76px; height: 36px;
    background: #fff; border: 1px solid var(--line); border-radius: 8px;
    font-size: 10px; color: var(--text);
    display: flex; align-items: center; justify-content: space-between; padding: 0 10px 0 12px;
  }
  .cta {
    position: absolute; left: 0; right: 0; bottom: 0; height: 44px; background: var(--yellow);
    display: flex; align-items: center; justify-content: center; gap: 8px;
    font-size: 19px; color: var(--ink);
  }
  .cta--bank { height: 46px; font-size: 16px; }

  .bank {
    position: absolute; left: 17px; width: 253px; height: 68px;
    background: #fff; border-radius: 8px;
    display: flex; align-items: center; padding-left: 18px;
  }
  .bank__mark { width: 26px; height: 26px; border-radius: 50%; background: #d9d9d9; margin-right: 20px; }
  .bank__name { font-size: 12.5px; font-weight: 600; color: var(--ink); }
  .bank__number { font-size: 10.5px; color: var(--text); margin-top: 2px; }
  .bank__more { position: absolute; right: 17px; top: 31px; display: flex; gap: 2px; }
  .bank__more span { width: 6px; height: 6px; border-radius: 50%; background: var(--dots); }
</style>
</head>
<body>

  <section class="screen loading loading--left">
    <div class="band band--top"></div>
    <div class="brand"><div class="brand__square"></div><div class="brand__name">Lendora</div></div>
    <h1 class="loading__title">Connecting to your bank...</h1>
    <p class="loading__body">Please don't exit the app. It takes 3-5 minutes to confirm your details with your bank.</p>
    <div class="band band--bottom"></div>
  </section>

  <section class="screen loading loading--right">
    <div class="band band--top"></div>
    <div class="brand"><div class="brand__square"></div><div class="brand__name">Lendora</div></div>
    <h1 class="loading__title">Connecting to your bank...</h1>
    <p class="loading__body">Please don't exit the app. It takes 3-5 minutes to confirm your details with your bank.</p>
    <div class="band band--bottom"></div>
  </section>

  <section class="screen app app--left">
    <header class="header">
      <svg class="header__back" viewBox="0 0 14 14"><path d="M9.5 1.5 4 7l5.5 5.5" fill="none" stroke="#555" stroke-width="1.6" stroke-linecap="round"/></svg>
      <span class="header__brand">Lendora</span>
      <div>
        <div class="header__title">Personal Details</div>
        <div class="header__sub">Please provide details as shown on ID</div>
      </div>
    </header>
    <div class="form">
      <label class="field__label" style="top:114px">Given Name</label>
      <div class="field__input" style="top:135px"></div>
      <label class="field__label" style="top:188px">Middle Name</label>
      <div class="field__input" style="top:209px"></div>
      <label class="field__label" style="top:261px">Sur Name</label>
      <div class="field__input" style="top:282px"></div>
      <label class="field__label" style="top:337px">Date of Birth</label>
      <div class="select" style="left:0">Day<svg width="9" height="6" viewBox="0 0 9 6"><path d="M1 1l3.5 3.5L8 1" fill="none" stroke="#333" stroke-width="1.2"/></svg></div>
      <div class="select" style="left:83px">Month<svg width="9" height="6" viewBox="0 0 9 6"><path d="M1 1l3.5 3.5L8 1" fill="none" stroke="#333" stroke-width="1.2"/></svg></div>
      <div class="select" style="left:166px">Year<svg width="9" height="6" viewBox="0 0 9 6"><path d="M1 1l3.5 3.5L8 1" fill="none" stroke="#333" stroke-width="1.2"/></svg></div>
    </div>
    <div class="cta">Next
      <svg width="26" height="12" viewBox="0 0 26 12"><path d="M1 6h23M19 1.5 24 6l-5 4.5" fill="none" stroke="#161616" stroke-width="1.4"/></svg>
    </div>
  </section>

  <section class="screen app app--right">
    <header class="header">
      <svg class="header__back" viewBox="0 0 14 14"><path d="M9.5 1.5 4 7l5.5 5.5" fill="none" stroke="#555" stroke-width="1.6" stroke-linecap="round"/></svg>
      <span class="header__brand">Lendora</span>
      <div class="header__title">Bank Details</div>
    </header>
    <div class="bank" style="top:86px">
      <div class="bank__mark"></div>
      <div><div class="bank__name">Harbor</div><div class="bank__number">256477897916554154</div></div>
      <div class="bank__more"><span></span><span></span><span></span></div>
    </div>
    <div class="bank" style="top:164px">
      <div class="bank__mark"></div>
      <div><div class="bank__name">Norvik</div><div class="bank__number">256477897916554154</div></div>
      <div class="bank__more"><span></span><span></span><span></span></div>
    </div>
    <div class="bank" style="top:243px">
      <div class="bank__mark"></div>
      <div><div class="bank__name">Southland Bank</div><div class="bank__number">256477897916554154</div></div>
      <div class="bank__more"><span></span><span></span><span></span></div>
    </div>
    <div class="cta cta--bank">
      <svg width="23" height="23" viewBox="0 0 23 23"><circle cx="11.5" cy="11.5" r="10.5" fill="none" stroke="#161616" stroke-width="1.3"/><path d="M11.5 6.5v10M6.5 11.5h10" stroke="#161616" stroke-width="1.3"/></svg>
      Connect Bank Account
    </div>
  </section>

</body>
</html>
```